Local primary school needs a flyer design for their fundraising fete

I need a flyer design for a local primary school holding a fundraising fete. I would like to see designs that feature the school logo, school colours (red white and navy) and that reference/mention the main rides and stalls at the event. If possible I would like the sponsors (on the newsletter supplied) to be included and the photo of the school available on the website. The final design should be easy for me to print and produce myself so that can leave at local shops, cafes etc. leading up to the event.

School

Font styles to use
Serif

Colors
ec2027
ffffff

```html
<!DOCTYPE html>
<html lang="en">
<head>
<meta charset="utf-8">
<title>Holy Cross Primary School Biannual Fete</title>
<link rel="stylesheet" href="https://fonts.googleapis.com/css2?family=Poiret+One&family=Permanent+Marker&family=Gloria+Hallelujah&display=swap">
<style>
  :root {
    --navy: #1c1a4a;
    --ink: #1a1430;
    --white: #ffffff;
    --red: #ec2027;
    --yellow: #ffe81a;
    --cyan: #3fdcec;
    --green: #26e22e;
    --band-grey: rgba(120,120,120,0.75);
    --sponsor-bg: #ffffff;
  }
  html, body { margin: 0; padding: 0; overflow: hidden; background: #ffffff; }
  .flyer {
    position: relative; width: 1200px; height: 900px; overflow: hidden;
    font-family: "Gloria Hallelujah", cursive;
  }
  .hero-photo {
    position: absolute; left: 0; top: 0; width: 1200px; height: 732px;
    background:
      linear-gradient(180deg, rgba(150,70,170,0.85) 0%, rgba(230,90,140,0.6) 22%, rgba(240,130,110,0.55) 38%, rgba(170,90,190,0.7) 60%, rgba(150,70,200,0.85) 100%),
      linear-gradient(90deg, #d57a6a 0%, #e8a07a 45%, #c96a9a 100%);
  }
  .abs { position: absolute; white-space: nowrap; }
  .title-line {
    left: 0; top: 6px; width: 1200px; text-align: center;
    font-family: "Poiret One", sans-serif; font-size: 58px; color: var(--white);
    letter-spacing: 1px;
  }
  .fete-word {
    left: 0; top: 90px; width: 1200px; text-align: center;
    font-family: "Permanent Marker", cursive; font-size: 150px; line-height: 1;
    color: var(--navy); letter-spacing: 62px; padding-left: 40px; box-sizing: border-box;
  }
  .intro { left: 320px; top: 248px; font-size: 28px; color: var(--white); }
  .ride { font-size: 24px; text-align: center; line-height: 64px; font-weight: bold; }
  .ride-castles { left: 195px; top: 285px; width: 210px; color: var(--yellow); }
  .ride-bungy { left: 460px; top: 285px; width: 190px; color: var(--cyan); font-size: 19px; }
  .ride-bull { left: 700px; top: 285px; width: 270px; color: var(--green); }
  .plus { font-size: 34px; color: var(--white); }
  .plus-one { left: 423px; top: 318px; }
  .plus-two { left: 665px; top: 318px; }
  .body-line { font-size: 27px; color: var(--ink); }
  .date { left: 232px; top: 418px; }
  .favourites { left: 30px; top: 482px; }
  .treats { left: 295px; top: 546px; }
  .stalls { left: 10px; top: 610px; }
  .excursion { left: 140px; top: 676px; }
  .school-photo {
    position: absolute; left: 0; top: 732px; width: 780px; height: 168px;
    background: linear-gradient(180deg, #9fb7cf 0%, #c8c2b8 55%, #7d7a72 100%);
  }
  .school-band {
    position: absolute; left: 165px; top: 780px; width: 470px; height: 80px;
    background: var(--band-grey);
  }
  .school-name { left: 175px; top: 788px; font-family: "Poiret One", sans-serif; font-size: 30px; color: var(--white); font-weight: bold; }
  .school-place { left: 175px; top: 826px; font-family: "Poiret One", sans-serif; font-size: 18px; color: var(--white); font-weight: bold; }
  .school-mark { position: absolute; left: 48px; top: 760px; }
  .mark-label { left: 16px; top: 870px; width: 146px; text-align: center; font-family: "Poiret One", sans-serif; font-size: 15px; color: var(--red); font-weight: bold; }
  .sponsors {
    position: absolute; left: 780px; top: 732px; width: 420px; height: 168px;
    background: var(--sponsor-bg);
    display: grid; grid-template-columns: repeat(3, 1fr); grid-auto-rows: 28px;
    align-items: center; padding: 6px 8px; box-sizing: border-box; gap: 0 6px;
  }
  .sponsor {
    font-family: "Poiret One", sans-serif; font-size: 15px; font-weight: bold;
    color: var(--navy); text-align: center; white-space: nowrap;
  }
</style>
</head>
<body>
<main class="flyer">
  <div class="hero-photo" role="img" aria-label="Photo of a child playing on an orange and purple jumping castle, tinted pink and purple"></div>

  <h1 class="abs title-line" style="margin:0;font-weight:normal;">Holy Cross Primary School Biannual</h1>
  <div class="abs fete-word">FETE!!</div>

  <div class="abs intro">+ Fantastic rides like . . .</div>
  <div class="abs ride ride-castles">Jumping<br>Castles</div>
  <div class="abs plus plus-one">+</div>
  <div class="abs ride ride-bungy">Horizontal<br>Bungy</div>
  <div class="abs plus plus-two">+</div>
  <div class="abs ride ride-bull">A WILD<br>BUCKING BULL</div>

  <div class="abs body-line date">+ Sunday 21st September 11:00am - 3:00pm</div>
  <div class="abs body-line favourites">+ all the old favourites. The petting zoo, The chocolate wheel as well as</div>
  <div class="abs body-line treats">all those other treats and delicious food.</div>
  <div class="abs body-line stalls">+ With over 20 stalls there'll be something for everyone. So come along</div>
  <div class="abs body-line excursion">for a family excursion filled with fun and some bargins</div>

  <div class="school-photo" role="img" aria-label="Photo of the modern school building with brick and glass frontage"></div>
  <svg class="school-mark" width="80" height="80" viewBox="0 0 80 80" aria-hidden="true">
    <circle cx="40" cy="40" r="38" fill="#ffffff" stroke="#ec2027" stroke-width="4"/>
  </svg>
  <div class="abs mark-label">Holy Cross</div>
  <div class="school-band"></div>
  <div class="abs school-name">Holy Cross Primary School</div>
  <div class="abs school-place">Linden, Canberra</div>

  <section class="sponsors" aria-label="Sponsors">
    <span class="sponsor">Birch &amp; Cole</span>
    <span class="sponsor">Plumbing</span>
    <span class="sponsor">Ridge Realty</span>
    <span class="sponsor">Westvale Motors</span>
    <span class="sponsor">CodeNest</span>
    <span class="sponsor">Aegean Club</span>
    <span class="sponsor">Lumi Hair</span>
    <span class="sponsor">Scoop Corner</span>
    <span class="sponsor">Onyx</span>
    <span class="sponsor">Halden Group</span>
    <span class="sponsor">Stride Shoes</span>
    <span class="sponsor">Deckworks</span>
    <span class="sponsor">Vantara</span>
    <span class="sponsor">The Quarry</span>
    <span class="sponsor">Gift Hamper Co</span>
    <span class="sponsor">Roam Travel</span>
  </section>
</main>
</body>
</html>
```